Clean Plinth Ads Banner Design For A Finance Company

Hi,
We're a UK based finance company and are looking for new banner ads to use on the Plinth Display Network.
We want the end product to stand out by using strong, minimal design - ideally starting from a dark theme, although I'm open to ideas.
The copy should read:
'Fast Bridging Loans From 0.39% PM'
Once we have these designs agreed, we are looking to replicate them for other products, changing only the text on each ad - for example, 'commercial mortgage service you can rely on' or 'development finance service you can rely on'.
The colours used on our website are the following:
Black - #040303
Orange - #f79124
White - #ffffff
Grey - #ffffff
Example ads that I like - https://www.brimcastle.com/wp-content/uploads/2021/07/plinth-display-ads-example-2-final.png.webp
2 - https://quendrahub.com/wp-content/uploads/2020/03/fbdd56ba3bd16c7a8debb13a411de786.jpg

```html
<!DOCTYPE html>
<html lang="en">
<head>
<meta charset="utf-8">
<title>Larkfield Finance – Bridging Loan Banners</title>
<link href="https://fonts.googleapis.com/css2?family=Open+Sans:wght@300;400;600;700;800&display=swap" rel="stylesheet">
<style>
  :root {
    --board: #dcdcdc;
    --black: #040303;
    --panel-light: #2b2b2b;
    --panel-dark: #0b0a0a;
    --orange: #f79124;
    --white: #ffffff;
    --label: #1e1e1e;
    --ring: #1c1b1b;
    --photo-a: #f3f5f7;
    --photo-b: #b9c9d8;
    --photo-c: #7d8fa3;
  }
  * { box-sizing: border-box; margin: 0; padding: 0; }
  html, body { width: 1200px; height: 1200px; overflow: hidden; }
  body {
    background: var(--board);
    font-family: "Open Sans", Arial, sans-serif;
    position: relative;
  }
  .size-label {
    position: absolute;
    font-size: 23px;
    font-weight: 400;
    color: var(--label);
    letter-spacing: 0.5px;
  }
  .banner {
    position: absolute;
    overflow: hidden;
    background: radial-gradient(ellipse at 50% 45%, var(--panel-light) 0%, #161515 60%, var(--panel-dark) 100%);
  }
  .badge-shape { position: absolute; overflow: visible; }
  .badge-shape .tail { fill: var(--orange); }
  .badge-shape .gap { fill: var(--ring); }
  .photo-fill { fill: url(#photoTone); }

  .brand {
    position: absolute;
    color: var(--orange);
    font-weight: 700;
    text-align: center;
    line-height: 1;
    letter-spacing: -0.5px;
  }
  .headline {
    position: absolute;
    color: var(--white);
    text-align: center;
    font-weight: 400;
    line-height: 1.12;
    letter-spacing: 0.2px;
  }
  .headline strong { font-weight: 700; }
  .rate-pill {
    position: absolute;
    background: var(--white);
    color: var(--black);
    font-weight: 800;
    border-radius: 999px;
    display: flex;
    align-items: center;
    justify-content: center;
    letter-spacing: 0.3px;
  }
  .cta {
    position: absolute;
    background: var(--orange);
    color: var(--white);
    font-weight: 700;
    border-radius: 999px;
    display: flex;
    align-items: center;
    letter-spacing: 0.3px;
  }
  .cta-icon {
    flex: none;
    border-radius: 50%;
    background: var(--black);
    display: flex;
    align-items: center;
    justify-content: center;
  }
  .cta-icon svg { display: block; }

  /* 300x600 skyscraper */
  .banner--tall { left: 46px; top: 115px; width: 360px; height: 720px; }
  .banner--tall .brand { left: 0; width: 360px; top: 28px; font-size: 34px; }
  .banner--tall .badge-shape { left: 0; top: 0; }
  .banner--tall .headline { left: 0; width: 360px; top: 483px; font-size: 34px; }
  .banner--tall .rate-pill { left: 70px; top: 575px; width: 222px; height: 44px; font-size: 34px; }
  .banner--tall .cta { left: 74px; top: 643px; width: 212px; height: 48px; font-size: 20px; padding-left: 8px; gap: 12px; }
  .banner--tall .cta-icon { width: 34px; height: 34px; }

  /* 336x280 rectangle */
  .banner--rect { left: 444px; top: 499px; width: 403px; height: 336px; }
  .banner--rect .brand { left: 14px; width: 150px; top: 26px; font-size: 24px; }
  .banner--rect .badge-shape { left: 0; top: 0; }
  .banner--rect .headline { left: 4px; width: 160px; top: 86px; font-size: 29px; line-height: 1.17; }
  .banner--rect .rate-pill { left: 14px; top: 228px; width: 147px; height: 30px; font-size: 23px; }
  .banner--rect .cta { left: 14px; top: 282px; width: 148px; height: 35px; font-size: 14px; padding-left: 5px; gap: 7px; }
  .banner--rect .cta-icon { width: 26px; height: 26px; }

  /* 930x180 leaderboard */
  .banner--wide { left: 47px; top: 929px; width: 1116px; height: 216px; }
  .banner--wide .brand { left: 60px; width: 170px; top: 73px; font-size: 36px; }
  .banner--wide .badge-shape { left: 0; top: 0; }
  .banner--wide .headline { left: 493px; width: 320px; top: 46px; font-size: 34px; }
  .banner--wide .rate-pill { left: 542px; top: 136px; width: 222px; height: 44px; font-size: 34px; }
  .banner--wide .cta { left: 840px; top: 84px; width: 210px; height: 48px; font-size: 20px; padding-left: 8px; gap: 12px; }
  .banner--wide .cta-icon { width: 34px; height: 34px; }
</style>
</head>
<body>

<svg width="0" height="0" style="position:absolute" aria-hidden="true">
  <defs>
    <linearGradient id="photoTone" x1="0" y1="0" x2="1" y2="1">
      <stop offset="0" stop-color="#5e7390"/>
      <stop offset="0.35" stop-color="#e9d2bf"/>
      <stop offset="0.6" stop-color="#f4f6f8"/>
      <stop offset="1" stop-color="#b9c9d8"/>
    </linearGradient>
  </defs>
</svg>

<div class="size-label" style="left:48px;top:68px;">300X600</div>
<section class="banner banner--tall">
  <div class="brand">Larkfield<br>Finance</div>
  <svg class="badge-shape" width="360" height="720" viewBox="0 0 360 720">
    <circle class="tail" cx="176" cy="281" r="174"/>
    <rect class="tail" x="176" y="281" width="174" height="174"/>
    <circle class="gap" cx="176" cy="281" r="150"/>
    <circle class="photo-fill" cx="176" cy="281" r="141" role="img" aria-label="Photo of a business handshake above a model house and documents"/>
  </svg>
  <div class="headline">FAST <strong>BRIDGING</strong><br><strong>LOANS</strong> FROM</div>
  <div class="rate-pill">0.39% PM</div>
  <div class="cta"><span class="cta-icon"><svg width="18" height="14" viewBox="0 0 18 14"><path d="M1 7h14M10 2l5 5-5 5" stroke="#fff" stroke-width="2.2" fill="none" stroke-linecap="round" stroke-linejoin="round"/></svg></span>LEARN MORE</div>
</section>

<div class="size-label" style="left:451px;top:442px;">336X280</div>
<section class="banner banner--rect">
  <div class="brand">Larkfield<br>Finance</div>
  <svg class="badge-shape" width="403" height="336" viewBox="0 0 403 336">
    <circle class="tail" cx="288" cy="169" r="118"/>
    <rect class="tail" x="288" y="169" width="118" height="118"/>
    <circle class="gap" cx="288" cy="169" r="102"/>
    <circle class="photo-fill" cx="288" cy="169" r="96" role="img" aria-label="Photo of a business handshake above a model house and documents"/>
  </svg>
  <div class="headline">FAST<br><strong>BRIDGING<br>LOANS</strong><br>FROM</div>
  <div class="rate-pill">0.39% PM</div>
  <div class="cta"><span class="cta-icon"><svg width="14" height="11" viewBox="0 0 18 14"><path d="M1 7h14M10 2l5 5-5 5" stroke="#fff" stroke-width="2.4" fill="none" stroke-linecap="round" stroke-linejoin="round"/></svg></span>LEARN MORE</div>
</section>

<div class="size-label" style="left:55px;top:891px;">930X180</div>
<section class="banner banner--wide">
  <div class="brand">Larkfield<br>Finance</div>
  <svg class="badge-shape" width="1116" height="216" viewBox="0 0 1116 216">
    <circle class="tail" cx="379" cy="97" r="104"/>
    <rect class="tail" x="379" y="97" width="104" height="119"/>
    <circle class="gap" cx="379" cy="97" r="90"/>
    <circle class="photo-fill" cx="379" cy="97" r="84" role="img" aria-label="Photo of a business handshake above a model house and documents"/>
  </svg>
  <div class="headline">FAST <strong>BRIDGING</strong><br><strong>LOANS</strong> FROM</div>
  <div class="rate-pill">0.39% PM</div>
  <div class="cta"><span class="cta-icon"><svg width="18" height="14" viewBox="0 0 18 14"><path d="M1 7h14M10 2l5 5-5 5" stroke="#fff" stroke-width="2.2" fill="none" stroke-linecap="round" stroke-linejoin="round"/></svg></span>LEARN MORE</div>
</section>

</body>
</html>
```